Bluefinch Painting needs a Website

We need a website built for a Painting company I own, we mainly do residential painting, but don't want to be limited to that.

Need to have estimate request form.
Need pic's of past projects

I like the look of the website for http://www.harborline-painters.example
& "Thistledown Property inspections"

My logo that was designed here on ArtHive on the front page

I would like one of the houses I downloaded as part of the background
of the front page.

Target Market(s)

Home owners

Industry/Entity Type

Painting

Number of Pages Required

1 page

Font styles to use
Serif

Requirements
Must have
• Estimate request form for home owners to fill out -
• Name:
• Phone Number:
• Address:
• E-mail:
• Painting project description:
• And my info to:
• My phone number: (555) 318-7764
• My web address bluefinchpainting.example
Nice to have
• My logo that was designed here on ArtHive

```html
<!DOCTYPE html>
<html lang="en">
<head>
<meta charset="utf-8">
<title>Bluefinch Painting</title>
<link rel="stylesheet" href="https://fonts.googleapis.com/css2?family=Cinzel:wght@400;700&family=Cormorant+Garamond:ital,wght@0,400;0,600;1,400&display=swap">
<style>
:root{
  --brand:#1b8ab3;
  --brand-dark:#0f5f85;
  --ink:#222;
  --muted:#777;
  --panel:#f1f1f1;
  --white:#fff;
  --cta-blue:#1c63c4;
  --cta-deep:#0f4aa3;
  --black:#111;
}
*{margin:0;padding:0;box-sizing:border-box}
html,body{width:1200px;height:2860px;overflow:hidden;background:var(--white)}
body{font-family:"Cormorant Garamond",Georgia,serif;color:var(--ink);position:relative}
.serif-caps{font-family:"Cinzel",Georgia,serif;text-transform:uppercase}

/* hero */
.hero{position:absolute;left:0;top:0;width:1200px;height:600px;
  background:linear-gradient(180deg,#3c4650 0%,#6a7470 30%,#8a8a80 55%,#5e6a58 80%,#44503e 100%)}
.topbar{position:absolute;left:0;top:0;width:1200px;height:100px;background:rgba(255,255,255,.9)}
.brand{position:absolute;left:70px;top:30px;display:flex;align-items:center;gap:12px}
.brand-mark{width:30px;height:30px;background:var(--brand)}
.brand-name{font-family:"Cinzel",serif;font-size:26px;font-weight:700;color:var(--brand-dark);letter-spacing:1px}
.nav{position:absolute;right:70px;top:40px;display:flex;gap:28px}
.nav a{font-family:"Cinzel",serif;font-size:20px;color:var(--brand);text-decoration:none}
.hero-title{position:absolute;left:0;width:1200px;top:300px;text-align:center;font-size:64px;color:var(--white);letter-spacing:2px}
.hero-btn{position:absolute;left:500px;top:400px;width:200px;height:56px;background:var(--brand);color:var(--white);
  font-family:"Cinzel",serif;font-size:18px;display:flex;align-items:center;justify-content:center}
.hero-card{position:absolute;right:0;top:430px;width:440px;height:170px;background:rgba(255,255,255,.85);text-align:right;padding:24px 40px}
.hero-card .brand-name{font-size:32px}
.hero-card p{font-size:24px;color:var(--ink);line-height:1.3}

/* section titles */
.sec-title{position:absolute;left:0;width:1200px;text-align:center;font-size:44px;color:var(--ink)}
.sec-sub{position:absolute;left:0;width:1200px;text-align:center;font-family:"Cinzel",serif;font-size:13px;color:var(--muted);letter-spacing:1px}

/* services */
.service{position:absolute;width:160px;text-align:center;top:770px}
.service svg{display:block;margin:0 auto 22px}
.service span{font-family:"Cinzel",serif;font-size:18px;color:var(--ink)}

/* about */
.about{position:absolute;left:0;top:950px;width:1200px;height:390px;background:var(--panel)}
.about .brand{left:400px;top:120px}
.about .brand-name{font-size:36px}
.about .brand-mark{width:40px;height:40px}
.contact{position:absolute;left:430px;display:flex;align-items:center;gap:18px;font-size:22px}
.contact svg{flex:none}

/* projects */
.project{position:absolute;width:252px;text-align:center}
.project .photo{width:252px;height:252px}
.project h3{font-size:22px;font-weight:600;margin-top:18px}
.project small{display:block;font-size:14px;color:var(--muted)}

/* contact form */
.interest{position:absolute;left:0;top:2252px;width:1200px;height:516px;
  background:linear-gradient(160deg,var(--cta-blue),var(--cta-deep) 60%,var(--cta-blue))}
.interest h2{position:absolute;left:0;top:40px;width:1200px;text-align:center;font-size:44px;color:var(--white);font-weight:400}
.interest .lede{position:absolute;left:0;top:96px;width:1200px;text-align:center;font-size:30px;font-style:italic;color:var(--white)}
.field{position:absolute;background:var(--white);height:42px;padding:0 14px;display:flex;align-items:center;
  font-family:"Cinzel",serif;font-size:13px;color:#999}
.field.area{align-items:flex-start;padding-top:14px}
.send{position:absolute;left:508px;top:2702px;width:200px;height:54px;background:var(--black);color:var(--white);
  font-family:"Cinzel",serif;font-size:18px;display:flex;align-items:center;justify-content:center}
.footer{position:absolute;left:0;top:2768px;width:1200px;height:92px;display:flex;align-items:center;justify-content:center;font-size:16px;color:var(--muted)}
</style>
</head>
<body>

<header class="hero" role="img" aria-label="Photo of a two-storey suburban house with garden in front">
  <div class="topbar">
    <div class="brand"><span class="brand-mark"></span><span class="brand-name">Bluefinch Painting</span></div>
    <nav class="nav"><a>Home</a><a>Services</a><a>Projects</a><a>About</a><a>Contact</a></nav>
  </div>
  <h1 class="hero-title serif-caps">We Proudly Use Quality</h1>
  <div class="hero-btn">TELL ME MORE</div>
  <div class="hero-card">
    <div class="brand-name">Bluefinch Painting</div>
    <p style="margin-top:14px">(555) 318-7764</p>
    <p>bluefinchpainting.example</p>
  </div>
</header>

<h2 class="sec-title serif-caps" style="top:650px">Services</h2>
<div class="sec-sub" style="top:712px">We Provide Quality</div>

<div class="service" style="left:210px">
  <svg width="60" height="70" viewBox="0 0 60 70"><rect x="8" y="4" width="44" height="26" fill="var(--brand)"/><rect x="8" y="30" width="44" height="8" fill="var(--brand-dark)"/><rect x="24" y="38" width="12" height="30" fill="var(--brand)"/></svg>
  <span>EXTERIOR</span>
</div>
<div class="service" style="left:420px">
  <svg width="70" height="70" viewBox="0 0 70 70"><rect x="4" y="6" width="52" height="18" rx="3" fill="var(--brand)"/><path d="M56 15h8v18H34v10" fill="none" stroke="var(--brand-dark)" stroke-width="4"/><rect x="29" y="43" width="10" height="25" fill="var(--brand)"/></svg>
  <span>INTERIOR</span>
</div>
<div class="service" style="left:620px">
  <svg width="60" height="70" viewBox="0 0 60 70"><path d="M8 14h44l-4 52H12z" fill="var(--brand)"/><ellipse cx="30" cy="14" rx="22" ry="6" fill="var(--brand-dark)"/><path d="M10 14c0-14 40-14 40 0" fill="none" stroke="var(--brand-dark)" stroke-width="3"/></svg>
  <span>RESIDENTIAL</span>
</div>
<div class="service" style="left:840px">
  <svg width="70" height="70" viewBox="0 0 70 70"><path d="M35 6 66 22 35 38 4 22z" fill="var(--brand)"/><path d="M4 34l31 16 31-16" fill="none" stroke="var(--brand)" stroke-width="6"/><path d="M4 46l31 16 31-16" fill="none" stroke="var(--brand-dark)" stroke-width="6"/></svg>
  <span>COMMERCIAL</span>
</div>

<section class="about">
  <h2 class="sec-title serif-caps" style="top:50px">About</h2>
  <div class="sec-sub" style="top:106px">Who We Are</div>
  <div class="brand"><span class="brand-mark"></span><span class="brand-name">Bluefinch Painting</span></div>
  <div class="contact" style="top:210px">
    <svg width="20" height="20" viewBox="0 0 20 20"><path d="M4 1l4 4-2 3c1 3 3 5 6 6l3-2 4 4-3 3C8 19 1 12 1 4z" fill="var(--ink)"/></svg>
    <span>(555) 318-7764</span></div>
  <div class="contact" style="top:264px">
    <svg width="20" height="16" viewBox="0 0 20 16"><rect width="20" height="16" fill="var(--ink)"/><path d="M1 1l9 8 9-8" fill="none" stroke="#fff" stroke-width="2"/></svg>
    <span>hello@bluefinchpainting.example</span></div>
  <div class="contact" style="top:318px">
    <svg width="20" height="20" viewBox="0 0 20 20"><circle cx="10" cy="10" r="9" fill="var(--ink)"/><path d="M1 10h18M10 1c-5 5-5 13 0 18M10 1c5 5 5 13 0 18" fill="none" stroke="#fff" stroke-width="1.4"/></svg>
    <span>www.bluefinchpainting.example</span></div>
</section>

<h2 class="sec-title serif-caps" style="top:1370px">Projects</h2>
<div class="sec-sub" style="top:1430px">Browse Our Completed Work</div>

<div class="project" style="left:188px;top:1480px">
  <div class="photo" role="img" aria-label="Photo of a freshly painted two-storey house exterior" style="background:linear-gradient(180deg,#c7d3de,#8f8672 55%,#5e6b4a)"></div>
  <h3>Exterior</h3><small>Family Home</small></div>
<div class="project" style="left:468px;top:1480px">
  <div class="photo" role="img" aria-label="Photo of an orange sofa against a white painted wall" style="background:linear-gradient(180deg,#ececec 45%,#e46a1e 55%,#b94d12)"></div>
  <h3>Interior</h3><small>Living Room</small></div>
<div class="project" style="left:748px;top:1480px">
  <div class="photo" role="img" aria-label="Photo of a house with garage and lawn under blue sky" style="background:linear-gradient(180deg,#4f8fd1,#8aa7bf 45%,#4e5a4c 70%,#4d7a34)"></div>
  <h3>Exterior</h3><small>Garage Front</small></div>
<div class="project" style="left:188px;top:1852px">
  <div class="photo" role="img" aria-label="Photo of a multi-storey apartment building with orange facade" style="background:linear-gradient(180deg,#e5eef6,#d98a4a 40%,#c0682e)"></div>
  <h3>Commercial</h3><small>Apartment Block</small></div>
<div class="project" style="left:468px;top:1852px">
  <div class="photo" role="img" aria-label="Photo of open paint cans in many bright colours" style="background:linear-gradient(135deg,#e83a8a,#f2c314 35%,#3cb34a 60%,#2a6fd6)"></div>
  <h3>Other</h3><small>Colour Mixing</small></div>
<div class="project" style="left:748px;top:1852px">
  <div class="photo" role="img" aria-label="Photo of a residential house with flowering garden" style="background:linear-gradient(180deg,#bcd3e8,#9a8c78 50%,#5c7a3c)"></div>
  <h3>Residential</h3><small>Suburban Home</small></div>

<section class="interest">
  <h2 class="serif-caps">Interested!</h2>
  <p class="lede">Tell us about your dream project!</p>
</section>
<div class="field" style="left:188px;top:2400px;width:396px">YOUR NAME *</div>
<div class="field" style="left:188px;top:2476px;width:396px">YOUR E-MAIL *</div>
<div class="field" style="left:188px;top:2548px;width:396px">YOUR PHONE #</div>
<div class="field" style="left:188px;top:2620px;width:396px">YOUR ADDRESS *</div>
<div class="field" style="left:608px;top:2400px;width:392px">TYPE OF PROJECT *</div>
<div class="field area" style="left:608px;top:2468px;width:392px;height:194px">YOUR MESSAGE *</div>
<div class="send">SEND MESSAGE</div>

<footer class="footer">© Copyright 2013 Bluefinch Painting</footer>
</body>
</html>
```